Chiropractor needs a snazzy business card

Business card for a chiropractic office.
Office treats patients of all ages.
Focus is on a natural lifestyle.
Colors can include the logo colors as well as white and a little orange.
Ideally the card would have something chiropractic related such as a spine.

The back of the card should have a items for making appointments (date, times....)

```html
<!DOCTYPE html>
<html lang="en">
<head>
<meta charset="utf-8">
<title>Meadowbrook Chiropractic – Business Card</title>
<link rel="stylesheet" href="https://fonts.googleapis.com/css2?family=Cinzel:wght@700&family=Crimson+Text:wght@400;600&family=Lato:wght@300;400&display=swap">
<style>
  :root {
    --page-bg: #ecebe6;
    --card-bg: #e7e6d7;
    --navy: #0f3f6b;
    --green: #58b54a;
    --ink: #1c1c1c;
    --rule: #8a8a7a;
    --leaf-soft: #b4d5a6;
    --leaf-warm: #eed9a4;
    --shadow: rgba(0,0,0,0.18);
  }
  * { margin: 0; padding: 0; box-sizing: border-box; }
  html, body { width: 1200px; height: 1000px; overflow: hidden; }
  body { background: var(--page-bg); position: relative; font-family: "Crimson Text", serif; }

  .card {
    position: absolute;
    width: 780px;
    height: 440px;
    background: var(--card-bg);
    box-shadow: 0 6px 18px var(--shadow);
    overflow: hidden;
  }
  .card--front { left: 200px; top: 40px; }
  .card--back  { left: 220px; top: 520px; }

  .holder-name {
    position: absolute; left: 72px; top: 58px;
    font-family: "Cinzel", serif; font-weight: 700;
    font-size: 40px; color: var(--navy); letter-spacing: 1px;
  }
  .phone-line {
    position: absolute; left: 72px; top: 118px;
    display: flex; align-items: center; gap: 18px;
  }
  .phone-number {
    font-family: "Lato", sans-serif; font-weight: 300; font-style: italic;
    font-size: 34px; letter-spacing: 9px; color: var(--green);
  }
  .icon { width: 26px; height: 26px; fill: var(--green); flex: none; }

  .address {
    position: absolute; left: 72px; top: 302px;
    display: flex; gap: 10px;
    font-size: 17px; line-height: 1.15; color: var(--ink);
  }
  .contact-list {
    position: absolute; left: 252px; top: 322px;
    display: flex; flex-direction: column; gap: 30px;
    font-size: 17px; color: var(--ink); list-style: none;
  }
  .contact-item { display: flex; align-items: center; gap: 16px; }

  .leaf-art {
    position: absolute; right: 0; bottom: 0;
    width: 330px; height: 330px;
    background: radial-gradient(circle at 70% 55%, var(--leaf-soft) 0%, var(--leaf-warm) 60%, rgba(231,230,215,0) 72%);
  }

  .wordmark {
    position: absolute; left: 0; right: 0; top: 70px;
    text-align: center;
    font-family: "Cinzel", serif; font-weight: 700; color: var(--navy);
  }
  .wordmark__name { font-size: 54px; letter-spacing: 2px; line-height: 1; }
  .wordmark__field { font-size: 28px; letter-spacing: 6px; margin-top: 8px; }

  .appointment {
    position: absolute; left: 110px; right: 110px; top: 240px;
    color: var(--ink);
  }
  .appointment__title {
    font-weight: 600; font-size: 20px; letter-spacing: 2px;
    color: var(--green); text-align: center; margin-bottom: 26px;
  }
  .appointment__row { display: flex; gap: 40px; margin-bottom: 28px; }
  .appointment__field {
    flex: 1; display: flex; align-items: flex-end; gap: 12px;
    font-size: 18px;
  }
  .appointment__line { flex: 1; border-bottom: 1px solid var(--rule); height: 20px; }
</style>
</head>
<body>

<section class="card card--front" aria-label="Card front">
  <h1 class="holder-name">PUT YOUR NAME</h1>
  <div class="phone-line">
    <svg class="icon" viewBox="0 0 24 24" aria-hidden="true"><path d="M6.6 10.8a15 15 0 0 0 6.6 6.6l2.2-2.2c.3-.3.7-.4 1-.2 1.1.4 2.3.6 3.6.6.6 0 1 .4 1 1V20c0 .6-.4 1-1 1A17 17 0 0 1 3 4c0-.6.4-1 1-1h3.5c.6 0 1 .4 1 1 0 1.3.2 2.5.6 3.6.1.3 0 .7-.2 1z"/></svg>
    <span class="phone-number">205-555-0147</span>
  </div>

  <div class="address">
    <svg class="icon" viewBox="0 0 24 24" aria-hidden="true"><path d="M12 2a7 7 0 0 0-7 7c0 5 7 13 7 13s7-8 7-13a7 7 0 0 0-7-7zm0 9.5A2.5 2.5 0 1 1 12 6.5a2.5 2.5 0 0 1 0 5z"/></svg>
    <p>1065 Put Your<br>Address Here<br>City Here<br>4582</p>
  </div>

  <ul class="contact-list">
    <li class="contact-item">
      <svg class="icon" viewBox="0 0 24 24" aria-hidden="true"><rect x="1" y="1" width="22" height="22" rx="4"/><g fill="none" stroke="#e7e6d7" stroke-width="1.3"><circle cx="12" cy="12" r="7"/><ellipse cx="12" cy="12" rx="3" ry="7"/><path d="M5 12h14M6 8.5h12M6 15.5h12"/></g></svg>
      <span>www.yourwebsite.com</span>
    </li>
    <li class="contact-item">
      <svg class="icon" viewBox="0 0 24 24" aria-hidden="true"><path d="M2 5h20v14H2z"/><path d="M2 5l10 8 10-8" fill="none" stroke="#e7e6d7" stroke-width="1.5"/></svg>
      <span>youremail@mailbox.com</span>
    </li>
  </ul>

  <div class="leaf-art" role="img" aria-label="Decorative figure formed by a round head and soft green and gold leaves"></div>
</section>

<section class="card card--back" aria-label="Card back">
  <div class="wordmark">
    <p class="wordmark__name">MEADOWBROOK</p>
    <p class="wordmark__field">CHIROPRACTIC</p>
  </div>

  <div class="appointment">
    <p class="appointment__title">YOUR NEXT APPOINTMENT</p>
    <div class="appointment__row">
      <div class="appointment__field"><span>Date</span><span class="appointment__line"></span></div>
      <div class="appointment__field"><span>Time</span><span class="appointment__line"></span></div>
    </div>
    <div class="appointment__row">
      <div class="appointment__field"><span>Date</span><span class="appointment__line"></span></div>
      <div class="appointment__field"><span>Time</span><span class="appointment__line"></span></div>
    </div>
  </div>
</section>

</body>
</html>
```